Fold up small biz card size flyer for Waxing Salon

To design a simple informative flyer which can fold 3 times measuring 2" x 9" for Waxing Salon in Toronto ON CanadaMy client would like both sides of flyer to have text i.e. the first half of flyer text on front and second half with address etc on back.She doesn;t want a company name as yet but would like maybe the simple shape of a body as in this sample deisign with a stone background.the other pics are just samples of ideas she has suggessted and if there is any text it should simply be wax or waxing or maybe body waxing.Please don't hesitate to ask quesition and i look forward to your submissions.

Target Market(s)

women amd men of all adult ages

Font styles to use
Serif
Sans Serif
Decorative
Script

Colors

Designer to choose colors to be used in the design.

Requirements
Must have
• Fold into three to biz card size so PLEASE STRICTLY 2 INCHES X 9 INCHES AND FOLDED DOWN TO A 2 X 3 BIZ CARD
• Due to small size of flyer there will have to be text on back as well
• thanks for your time and patience
Nice to have
• the images are simply ideas of existing brands...just stone background with perhadps small body shaped graphic no company name
Should not have
• scanitly clad women preferably small body shoped graphic only please/

```html
<!DOCTYPE html>
<html lang="en">
<head>
<meta charset="utf-8">
<title>Body Waxing Flyer</title>
<link href="https://fonts.googleapis.com/css2?family=Dancing+Script:wght@600;700&family=Montserrat:wght@400;700&display=swap" rel="stylesheet">
<style>
:root{
  --bg:#f8dfea;
  --bg-deep:#e9a9c6;
  --petal:#dc6f9f;
  --script:#e32d86;
  --purple:#7b4ca3;
  --ink:#3a3338;
  --tick:#e8358a;
  --frame:#f2b7cc;
  --frame-strong:#ef9fb7;
  --divider:#d8c2e2;
  --panel:rgba(255,255,255,.35);
}
*{margin:0;padding:0;box-sizing:border-box}
html,body{width:1200px;height:5391px;overflow:hidden}
body{position:relative;background:var(--bg);font-family:'Montserrat',sans-serif;color:var(--ink)}
.petals{position:absolute;inset:0;background:
  radial-gradient(ellipse 420px 520px at 1200px 0px,var(--petal),transparent 70%),
  radial-gradient(ellipse 380px 700px at 0px 1100px,rgba(220,111,159,.55),transparent 70%),
  radial-gradient(ellipse 500px 600px at 1200px 2000px,rgba(233,169,198,.7),transparent 70%),
  radial-gradient(ellipse 480px 520px at 1200px 3700px,rgba(220,111,159,.7),transparent 70%),
  radial-gradient(ellipse 420px 560px at 0px 4700px,rgba(233,169,198,.7),transparent 70%);}
.abs{position:absolute}
.mid{transform:translateY(-50%);white-space:nowrap}
.script{font-family:'Dancing Script',cursive;font-weight:700;color:var(--script);left:0;width:1200px;text-align:center}
.offer-box{left:220px;top:255px;width:712px;height:1530px;border:2px solid var(--frame);background:rgba(255,255,255,.25)}
.offer{left:370px}
.offer-title{font-weight:700;color:var(--purple);font-size:54px}
.offer-title.big{font-size:66px}
.offer-line{font-size:42px;line-height:72px}
.value-band{left:0;top:1784px;width:1200px;height:160px;background:rgba(233,169,198,.45)}
.deal-panel{left:0;top:1943px;width:1200px;height:210px;background:var(--panel);border-top:2px solid var(--frame);border-bottom:2px solid var(--frame)}
.deal-text{left:287px;top:1958px;font-weight:700;color:var(--purple);font-size:44px;line-height:63px}
.list-box{border:2px solid var(--frame);background:rgba(255,255,255,.2)}
.services{list-style:none;font-size:38px;line-height:62px}
.services li{display:flex;align-items:center;gap:14px;white-space:nowrap}
.services svg{width:44px;height:44px;flex:none}
.note-title{left:716px;top:2894px;font-weight:700;color:var(--purple);font-size:36px}
.note{left:725px;font-size:38px}
.fine{font-size:23px;color:var(--ink)}
.address-box{left:237px;top:3912px;width:714px;height:1110px;border:6px solid var(--frame-strong)}
.address-divider{left:243px;top:4383px;width:702px;height:40px;background:var(--divider)}
.address{left:337px;font-size:46px;line-height:66px}
.footer{left:0;top:5156px;width:1200px;height:205px;background:#fff}
.web{left:0;top:5256px;width:1200px;text-align:center;font-weight:700;color:var(--purple);font-size:66px}
</style>
</head>
<body>
<svg width="0" height="0" style="position:absolute"><symbol id="tick" viewBox="0 0 24 24"><path d="M3 13l6 6L21 4" fill="none" stroke="#e8358a" stroke-width="3.6" stroke-linecap="round" stroke-linejoin="round"/></symbol></svg>
<div class="petals" role="img" aria-label="Soft pink flower petal background"></div>

<div class="abs script mid" style="top:105px;font-size:76px">Door buster Deal !</div>
<div class="abs offer-box"></div>
<div class="abs offer offer-title mid" style="top:300px">$66 Body Waxing</div>
<div class="abs offer" style="top:343px">
  <div class="offer-line">For women only</div>
  <div class="offer-line">(Neck to Toe -</div>
  <div class="offer-line">Including Brazilian)</div>
  <div class="offer-line">with Take Home Scrub</div>
  <div class="offer-line">used to improve</div>
  <div class="offer-line">in-grown body hair.</div>
  <div class="offer-line">($120 value)</div>
</div>
<div class="abs offer offer-title big mid" style="top:947px">Guests receive</div>
<div class="abs offer" style="top:990px">
  <div class="offer-line">&nbsp;full body waxing</div>
  <div class="offer-line">during one appointment</div>
  <div class="offer-line">&nbsp;on the following areas:</div>
  <div class="offer-line">&nbsp;butt, hollywood, bikini,</div>
  <div class="offer-line">underarms, stomach,</div>
  <div class="offer-line">cleavage, full back,</div>
  <div class="offer-line">full arms &amp; full legs.</div>
</div>
<div class="abs offer offer-title mid" style="top:1600px">$66 Body Polishing</div>
<div class="abs offer" style="top:1640px">
  <div class="offer-line">The secret to soft,</div>
  <div class="offer-line">&nbsp;smooth skin.</div>
</div>

<div class="abs value-band"></div>
<div class="abs script mid" style="top:1860px;font-size:78px">Unbeatable Value !</div>
<div class="abs deal-panel"></div>
<div class="abs deal-text">
  <div>Spa Treatments - $13 each</div>
  <div>when you purchase 5</div>
  <div>services&nbsp; or more from list below</div>
</div>

<div class="abs list-box" style="left:38px;top:2194px;width:626px;height:1370px"></div>
<ul class="abs services" style="left:62px;top:2205px">
  <li><svg><use href="#tick"/></svg>Back Massage</li>
  <li><svg><use href="#tick"/></svg>Back Scrub</li>
  <li><svg><use href="#tick"/></svg>Spa Manicure</li>
  <li><svg><use href="#tick"/></svg>Full Brazilian Wax</li>
  <li><svg><use href="#tick"/></svg>Full 60 Minute Facial</li>
  <li><svg><use href="#tick"/></svg>Face Polishing</li>
  <li><svg><use href="#tick"/></svg>Face Bleaching</li>
  <li><svg><use href="#tick"/></svg>Scalp &amp; Hair Oil Massage</li>
  <li><svg><use href="#tick"/></svg>Dry Hair Treatment</li>
  <li><svg><use href="#tick"/></svg>Hair Colour Application</li>
  <li><svg><use href="#tick"/></svg>Four Inch Henna Tattoo</li>
  <li><svg><use href="#tick"/></svg>Eyebrow Tinting/Shaping</li>
  <li><svg><use href="#tick"/></svg>Upper Lip Thread/wax</li>
  <li><svg><use href="#tick"/></svg>Forehead Thread/wax</li>
  <li><svg><use href="#tick"/></svg>Side Burn Thread/Wax</li>
  <li><svg><use href="#tick"/></svg>Full Face Thread/Wax</li>
  <li><svg><use href="#tick"/></svg>Nostril Wax</li>
  <li><svg><use href="#tick"/></svg>Nape Wax</li>
  <li><svg><use href="#tick"/></svg>Cleavage Wax</li>
  <li><svg><use href="#tick"/></svg>Stomach Wax</li>
  <li><svg><use href="#tick"/></svg>Upper Back Wax</li>
</ul>

<div class="abs list-box" style="left:664px;top:2194px;width:496px;height:633px"></div>
<ul class="abs services" style="left:674px;top:2230px">
  <li><svg><use href="#tick"/></svg>&nbsp;Lower Back Wax</li>
  <li><svg><use href="#tick"/></svg>Underarm Wax</li>
  <li><svg><use href="#tick"/></svg>&nbsp;Half Arm Wax</li>
  <li><svg><use href="#tick"/></svg>Full Arm Wax</li>
  <li><svg><use href="#tick"/></svg>Half Legs Wax</li>
  <li><svg><use href="#tick"/></svg>Full Legs Wax</li>
  <li><svg><use href="#tick"/></svg>Bikini Line Wax</li>
  <li><svg><use href="#tick"/></svg>Bum Wax</li>
  <li><svg><use href="#tick"/></svg>Hollywood Wax</li>
</ul>

<div class="abs note-title mid">Note</div>
<div class="abs note mid" style="top:2955px">$5 extra for nail polish</div>
<div class="abs note mid" style="top:3018px">counts as 2 services</div>
<div class="abs note mid" style="top:3080px">counts as 3 services</div>
<div class="abs fine mid" style="left:794px;top:3193px">Services may be</div>
<div class="abs fine mid" style="left:794px;top:3256px">Shared with your</div>
<div class="abs fine mid" style="left:844px;top:3318px">Loved Ones</div>
<div class="abs fine mid" style="left:824px;top:3380px">Some conditions apply</div>

<div class="abs script mid" style="top:3776px;font-size:82px;font-weight:600">Call today to book a spot.</div>
<div class="abs address-box"></div>
<div class="abs address" style="top:3939px">
  <div>2417 MAPLEWOOD ST EAST</div>
  <div>#3&nbsp; Toronto</div>
  <div>ON&nbsp; M4X 3B7</div>
  <div>Opp to Saffron Grill House</div>
  <div>(416) 555-0142</div>
  <div>1 (833) 555-0178</div>
</div>
<div class="abs address-divider"></div>
<div class="abs address" style="top:4467px">
  <div>3852 Cedarbrook Ave,</div>
  <div>#3.&nbsp; North York,</div>
  <div>ON&nbsp; M4Y 5K8</div>
  <div>Opp to Northgate Mall</div>
  <div>Next to Quickway</div>
  <div>(416) 555-0193.</div>
  <div>1 (833) 555-0164</div>
</div>

<div class="abs footer"></div>
<div class="abs web mid">www.smoothbodywax.com</div>
</body>
</html>
```